Napa Winery - Chardonnay wine label

We are looking for a label for a new Napa Valley winery - chardonnay wine. The winery is "Marrowbrook Hill Vintners" and we would like to see it depicted on a white wine (chardonnay style) bottle. The winery is called Marrowbrook Hill Vintners.

We are open to ideas!

Target Market(s)

High-end chardonnay lovers

Requirements
Nice to have
• Painted or etched label onto bottle

```html
<!DOCTYPE html>
<html lang="en">
<head>
<meta charset="utf-8">
<title>Marrowbrook Hill Vintners – Chardonnay Label</title>
<link rel="stylesheet" href="https://fonts.googleapis.com/css2?family=Pinyon+Script&family=Libre+Caslon+Text:wght@400&family=La+Belle+Aurore&display=swap">
<style>
  :root {
    --backdrop: #eeede8;
    --label-paper: #ffffff;
    --ink: #1f1f1f;
    --ink-soft: #5a5a5a;
    --body-grey: #8a8a8a;
    --gold-rule: #d9b15a;
    --etch-dark: #6e6e6e;
    --etch-light: #d4d4d4;
  }
  html, body {
    margin: 0;
    padding: 0;
    width: 1065px;
    height: 1200px;
    overflow: hidden;
    background: var(--backdrop);
  }
  .canvas {
    position: relative;
    width: 1065px;
    height: 1200px;
  }
  .wine-label {
    position: absolute;
    left: 82px;
    top: 171px;
    width: 900px;
    height: 858px;
    background: var(--label-paper);
    box-shadow: 0 2px 10px rgba(0, 0, 0, 0.08);
    text-align: center;
    color: var(--ink);
  }
  .winery-name {
    position: absolute;
    top: 62px;
    left: 0;
    right: 0;
    margin: 0;
    font-family: "Pinyon Script", cursive;
    font-weight: 400;
    font-size: 74px;
    line-height: 1;
    color: var(--ink);
  }
  .estate-illustration {
    position: absolute;
    top: 190px;
    left: 115px;
    width: 670px;
    height: 300px;
  }
  .varietal {
    position: absolute;
    top: 550px;
    left: 0;
    right: 0;
    margin: 0;
    font-family: "Libre Caslon Text", serif;
    font-weight: 400;
    font-size: 48px;
    letter-spacing: 1px;
    line-height: 1;
  }
  .appellation {
    position: absolute;
    top: 612px;
    left: 0;
    right: 0;
    margin: 0;
    font-family: "La Belle Aurore", cursive;
    font-size: 40px;
    line-height: 1;
    color: var(--ink-soft);
  }
  .gold-rule {
    position: absolute;
    top: 702px;
    left: 318px;
    width: 264px;
    height: 3px;
    background: var(--gold-rule);
  }
  .tasting-note {
    position: absolute;
    top: 716px;
    left: 130px;
    width: 640px;
    margin: 0;
    font-family: "Libre Caslon Text", serif;
    font-size: 19.5px;
    line-height: 33px;
    color: var(--body-grey);
  }
</style>
</head>
<body>
  <main class="canvas">
    <section class="wine-label">
      <h1 class="winery-name">Marrowbrook Hill Vintners</h1>

      <svg class="estate-illustration" viewBox="0 0 670 300" role="img"
           aria-label="Etched pen sketch of a hilltop château with towers above rows of vines stretching toward the viewer">
        <defs>
          <radialGradient id="etch-tone" cx="50%" cy="62%" r="55%">
            <stop offset="0%" stop-color="var(--etch-dark)"/>
            <stop offset="60%" stop-color="var(--etch-light)"/>
            <stop offset="100%" stop-color="#ffffff" stop-opacity="0"/>
          </radialGradient>
        </defs>
        <ellipse cx="335" cy="180" rx="335" ry="120" fill="url(#etch-tone)"/>
      </svg>

      <h2 class="varietal">CHARDONNAY</h2>
      <p class="appellation">Napa Valley</p>
      <div class="gold-rule"></div>
      <p class="tasting-note">
        Golden and bright, with ripe pear, baked apple and a touch of oak,
        this hillside chardonnay finishes long, creamy and gently spiced
        with toasted hazelnut notes.
      </p>
    </section>
  </main>
</body>
</html>
```